Brevik Plant Traders Company - Enhance our webpage

We have an existing website - please see www.brockwaytooling.com. The text in there is fundamentally what we want to say. There is also a search function where you can search our database, which is crucial to the site. We are happy with our logo, top left-hand side and want it to remain as it is. Everything else, including pictures, drawings and animation can be changed. In general, the website looks a little tired and the icons on the tabs need creative input.

We want our website to look dynamic, eye-catching, bold, very professional, modern and also uphold our impeccable 30-year reputation in the business.

We are essentially looking for a young, dynamic mind to provide our website with some inspiration. We encourage all designers to use their imagination and surprise us.

We have technical people to do the technical work, such as coding, but what we are looking for is asthetic creativity.

In addition, we have seen our competitors offer a translation service on their website i.e. you can just click on a flag and the website will turn into a different language. If you can incorporate this, it would be very useful.
Updates

Reason: Hi All - we have received some fantastic designs, so thank you. We are extending the deadline so that people can upgrade theirs slightly. We haven't seen enough dynamism with pictures and icons. And for those who have shown dynamism in those departments, we would also like you to consider including a video on the home page of some sort. You can find many videos of working machines like these on Clip-Spool. Thanks.

Target Market(s)

International Engineering companies

Industry/Entity Type

Flag

Requirements
Must have
• The "search database" facility must remain there.
Nice to have
• Perhaps some working videos running on the homepage of some of the types of machines we sell. You can find many such videos on ClipSpool. We will constantly change those as we get new stock in.

```html
<!DOCTYPE html>
<html lang="en">
<head>
<meta charset="utf-8">
<title>Brockway Tooling</title>
<link href="https://fonts.googleapis.com/css2?family=Ubuntu:wght@300;400;500;700&family=Questrial&family=Roboto+Condensed:wght@300;400&display=swap" rel="stylesheet">
<style>
:root{
  --dark:#2a2a2a;
  --dark-2:#3a3a3a;
  --red:#c40f14;
  --red-dark:#a80b10;
  --page:#f1f1f1;
  --panel:#e7e7e7;
  --ink:#333;
  --muted:#666;
  --faint:#9a9a9a;
  --white:#fff;
}
*{margin:0;padding:0;box-sizing:border-box}
html,body{width:1200px;height:1029px;overflow:hidden;background:var(--page)}
.stage{width:1400px;height:1200px;transform:scale(0.857143);transform-origin:0 0;position:relative;font-family:"Ubuntu",sans-serif;color:var(--ink);background:var(--page)}
.abs{position:absolute}
.topbar{left:0;top:0;width:1400px;height:38px;background:var(--dark);color:var(--white);font-size:13px}
.topbar .url{left:241px;top:11px;font-size:14px;font-weight:300}
.topbar .lang{left:916px;top:12px;font-size:12px}
.topbar .lang em{font-style:normal;color:var(--red);margin-left:10px}
.topbar .links{left:1088px;top:12px;font-size:12px}
.header{left:0;top:38px;width:1400px;height:176px;background:linear-gradient(180deg,#303030,#3c3c3c 60%,#2e2e2e)}
.brand{left:241px;top:72px;font-size:38px;font-weight:700;color:var(--white);letter-spacing:.5px}
.search{left:911px;top:80px;width:277px;height:31px;background:#f4f4f4;border:2px solid #cfcfcf;border-radius:3px}
.search span{position:absolute;left:9px;top:7px;font-size:11px;color:#aaa;font-weight:300}
.search .btn{position:absolute;right:1px;top:1px;width:46px;height:25px;background:#2b2b2b;border-radius:2px}
.nav{left:211px;top:151px;width:979px;height:63px;background:linear-gradient(180deg,var(--red),var(--red-dark));border-radius:6px 6px 0 0}
.nav-item{position:absolute;top:0;width:160px;margin-left:-80px;text-align:center;color:var(--white);font-size:14px}
.nav-item svg{display:block;margin:12px auto 4px}
.hero{left:211px;top:214px;width:979px;height:376px;background:linear-gradient(90deg,#ffffff 0%,#f7f7f7 45%,#ececec 100%)}
.hero h1{position:absolute;left:47px;top:74px;font-family:"Questrial",sans-serif;font-weight:400;font-size:36px;line-height:34px;color:#3a3a3a}
.hero .sub{position:absolute;left:49px;top:146px;font-family:"Questrial",sans-serif;font-size:15px;letter-spacing:.5px}
.hero p{position:absolute;left:49px;top:182px;width:340px;font-family:"Questrial",sans-serif;font-size:13px;line-height:18px;color:var(--faint);text-transform:uppercase}
.hero .more{position:absolute;left:49px;top:298px;font-family:"Roboto Condensed",sans-serif;font-size:22px;color:#444;letter-spacing:-.5px;display:flex;align-items:center;gap:8px}
.hero .photo{position:absolute;left:470px;top:6px;width:460px;height:364px;border-radius:10px;background:radial-gradient(ellipse at 55% 50%,#dcdfe3 0%,#eef0f2 60%,rgba(240,240,240,0) 75%)}
.bar{left:210px;width:980px;height:42px;background:var(--panel);border-top:1px solid #dcdcdc}
.bar h2{position:absolute;left:19px;top:10px;font-family:"Roboto Condensed",sans-serif;font-weight:400;font-size:20px;color:#3a3a3a}
.products{left:211px;top:650px;width:982px;height:215px;background:var(--white);border:1px solid #e0e0e0}
.product{position:absolute;top:16px;width:200px;text-align:center;font-size:12px}
.product .thumb{height:150px;margin-bottom:17px}
.video{left:210px;top:955px;width:351px;height:182px;border:3px solid #333;border-radius:3px;background:linear-gradient(110deg,#2a2a2a 0%,#5a5a5a 35%,#c9c9c9 60%,#f0f0f0 80%,#9a9a9a 100%)}
.video .play{position:absolute;left:150px;top:64px;width:48px;height:34px;background:rgba(20,20,20,.85);border-radius:8px}
.about{left:581px;top:951px;width:600px;font-size:12px;font-weight:300;line-height:14.5px;color:#444}
.about p{margin-bottom:14.5px}
.footer{left:210px;top:1159px;width:980px;height:41px;background:var(--panel);text-align:center;font-size:12px;font-weight:300;color:#888;padding-top:7px;line-height:15px}
</style>
</head>
<body>
<div class="stage">
  <div class="abs topbar">
    <div class="abs url">www.brockwaytooling.com</div>
    <div class="abs lang">Select Language <em>English</em> <span>▾</span></div>
    <div class="abs links">About Us | Enquiry</div>
  </div>

  <div class="abs header"></div>
  <div class="abs brand">Brockway Tooling</div>
  <div class="abs search">
    <span>Type any machine name / make / model</span>
    <div class="btn"><svg width="46" height="25" viewBox="0 0 46 25"><circle cx="22" cy="11.5" r="3.5" fill="none" stroke="#fff" stroke-width="1.8"/><line x1="24.5" y1="14" x2="27" y2="16.5" stroke="#fff" stroke-width="2"/></svg></div>
  </div>

  <nav class="abs nav">
    <div class="nav-item" style="left:68px">
      <svg width="26" height="22" viewBox="0 0 26 22"><path d="M2 11 L13 2 L24 11" fill="none" stroke="#fff" stroke-width="3"/><path d="M6 11 V21 H11 V15 H15 V21 H20 V11" fill="#fff"/></svg>Home</div>
    <div class="nav-item" style="left:256px">
      <svg width="24" height="22" viewBox="0 0 24 24"><circle cx="12" cy="12" r="8" fill="none" stroke="#fff" stroke-width="5" stroke-dasharray="3 3.3"/><circle cx="12" cy="12" r="6" fill="#fff"/><circle cx="12" cy="12" r="2.5" fill="#b80d12"/></svg>Used Machines</div>
    <div class="nav-item" style="left:484px">
      <svg width="34" height="22" viewBox="0 0 34 22"><circle cx="12" cy="12" r="7.5" fill="none" stroke="#fff" stroke-width="5" stroke-dasharray="3 2.9"/><circle cx="12" cy="12" r="5.5" fill="#fff"/><circle cx="12" cy="12" r="2.5" fill="#b80d12"/><circle cx="26" cy="8" r="4.5" fill="none" stroke="#fff" stroke-width="3" stroke-dasharray="2 1.8"/><circle cx="26" cy="8" r="1.5" fill="#fff"/></svg>New CNC Machines</div>
    <div class="nav-item" style="left:713px">
      <svg width="24" height="22" viewBox="0 0 24 24"><circle cx="12" cy="12" r="9.5" fill="none" stroke="#fff" stroke-width="2"/><circle cx="12" cy="12" r="4" fill="none" stroke="#fff" stroke-width="2"/><path d="M12 2.5 V8 M12 16 V21.5 M2.5 12 H8 M16 12 H21.5" stroke="#fff" stroke-width="3"/></svg>Manufacturing</div>
    <div class="nav-item" style="left:900px">
      <svg width="24" height="22" viewBox="0 0 24 24"><circle cx="12" cy="12" r="10" fill="none" stroke="#fff" stroke-width="2"/><path d="M8.5 6.5 L10.5 9 L9.5 10.5 Q11 13.5 13.5 14.5 L15 13.5 L17.5 15.5 L16 17.5 Q10 17 6.5 9.5 Z" fill="#fff"/></svg>Contact</div>
  </nav>

  <section class="abs hero">
    <h1>CNC-SURFACE<br>GRINDER.</h1>
    <div class="sub">NOW AVAILABLE</div>
    <p>Lorem ipsum est simplement du faux texte employé dans la composition et la mise en page avant impression. Le Lorem Ipsum est le faux texte standard de l'imprimerie</p>
    <div class="more">FIND OUR MORE
      <svg width="24" height="18" viewBox="0 0 24 18"><path d="M2 2 L9 9 L2 16 M9 2 L16 9 L9 16 M15 2 L22 9 L15 16" fill="none" stroke="#c40f14" stroke-width="3.2"/></svg></div>
    <div class="photo" role="img" aria-label="CNC surface grinding machine, white cabinet with blue trim and control panel"></div>
  </section>

  <div class="abs bar" style="top:609px"><h2>FEATURED PRODUCT</h2></div>
  <div class="abs products">
    <div class="product" style="left:31px"><div class="thumb" role="img" aria-label="Green cylindrical grinder in a workshop" style="background:linear-gradient(135deg,#bfe0e6,#7fae8a 50%,#5d8a68)"></div>Cylindrical Grinder</div>
    <div class="product" style="left:270px"><div class="thumb" role="img" aria-label="Cylindrical grinder with yellow wheel guard" style="background:linear-gradient(135deg,#e6e01a,#d8d20e 45%,#8c8f94 75%,#5d6165)"></div>Cylindrical Grinder</div>
    <div class="product" style="left:509px"><div class="thumb" role="img" aria-label="Long green lathe bed grinder on shop floor" style="background:linear-gradient(135deg,#6f7f6a,#9cbfa0 45%,#7a9c82 75%,#54604f)"></div>Cylindrical Grinder</div>
    <div class="product" style="left:748px"><div class="thumb" role="img" aria-label="Large green grinding machine in a factory hall" style="background:linear-gradient(135deg,#4a4a44,#7c8e80 45%,#6b7c6e 70%,#3b3b36)"></div>Cylindrical Grinder</div>
  </div>

  <div class="abs bar" style="top:887px;height:44px"><h2>WELCOME TO BROCKWAY TOOLING</h2></div>

  <div class="abs video" role="img" aria-label="Video of a machine tool spindle at work">
    <div class="play"><svg width="48" height="34" viewBox="0 0 48 34"><path d="M19 10 L31 17 L19 24 Z" fill="#fff"/></svg></div>
  </div>

  <div class="abs about">
    <p>Brockway Tooling is an established vendor of new and used machine tools, with over 30 years' experience in buying, rebuilding, retrofitting and commissioning machine tools WORLDWIDE. We have industrial space both in London and Mumbai, where we store over 200 machines at any given time. We specialise in gear manufacturing, pressure diecasting, plano miller, boring and grinding machines, as well as heat treatment facilities, machining and turning centres. Such machines find their usage in the automotive, aviation, power generation, mining and construction industries. Our stock includes the industry's best brands such as Galston, Pfennig, Harten and Bauer. The stock comprises both CNC and conventional machines.</p>
    <p>We are a global leader in the production of new CNC machines, as we retrofit conventional machines into affordable CNC machine tools.</p>
    <p>We also have a gear manufacturing facility in Mumbai, producing quality bespoke gears for some of India's leading Original Equipment Manufacturers. We can produce gears from 16mm to 1600 mm in diameter.</p>
  </div>

  <footer class="abs footer">
    Home | About Us | Used Machines | Manufacturing | New CNC Machines | Enquiry | Contact Us | Sitemap<br>
    Copyright. Brockway Tooling. All Rights Reserved.
  </footer>
</div>
</body>
</html>
```